Home Security Company Business Card

Looking for a eye catching business card that is non traditional and stands out but yet still looks professional. It should include all the pertinent information such as name, title, address, telephone, e-mail, website address should definitely stand out and then finally the logo.

Target Market(s)

Residential and Commercial accounts mostly upscale accounts

Industry/Entity Type

Security

Contact Information for Business Card

Name
Title
Address
Office #
Cell #
E-mail
Website

Font styles to use
Serif
Sans Serif

Requirements
Must have
• Logo, two sided color configuration
Nice to have
• You decide
Should not have
• There really aren't any.

```html
<!DOCTYPE html>
<html lang="en">
<head>
<meta charset="utf-8">
<title>Hearthwall Security Systems – Business Card</title>
<link href="https://fonts.googleapis.com/css2?family=Cinzel:wght@600&family=Questrial&family=Open+Sans:wght@600&display=swap" rel="stylesheet">
<style>
  :root{
    --bg:#e9e4dc;
    --paper:#ffffff;
    --red:#9a1f1b;
    --red-dark:#6e1210;
    --red-light:#b0302a;
    --gold:#e3a63a;
    --gold-light:#f2c766;
    --ink-light:#fbeeee;
    --muted:#f0c9c4;
  }
  *{margin:0;padding:0;box-sizing:border-box}
  html,body{width:1200px;height:1023px;overflow:hidden}
  body{background:var(--bg);display:flex;align-items:center;justify-content:center;gap:50px;font-family:"Questrial",sans-serif}
  .card{width:540px;height:310px;position:relative;overflow:hidden;box-shadow:0 6px 18px rgba(0,0,0,.18)}
  /* front */
  .card-front{background:var(--paper)}
  .front-brand{position:absolute;left:34px;top:34px;color:var(--red);font-family:"Cinzel",serif;font-weight:600;line-height:1}
  .front-brand .brand-main{display:block;font-size:44px;letter-spacing:1px}
  .front-brand .brand-sub{display:block;font-size:17px;margin-top:6px;letter-spacing:.5px}
  .gold-corner{position:absolute;right:0;top:0;width:150px;height:120px;background:linear-gradient(90deg,var(--gold-light),var(--gold))}
  .front-band{position:absolute;left:0;right:0;top:120px;height:160px;background:linear-gradient(180deg,var(--red-light),var(--red) 60%,var(--red-dark))}
  .logo-spot{position:absolute;right:38px;top:72px;width:74px;height:74px;border-radius:50%;background:var(--gold);border:4px solid var(--paper)}
  .person{position:absolute;left:34px;top:22px;color:var(--ink-light)}
  .person-name{font-family:"Open Sans",sans-serif;font-weight:600;font-size:17px}
  .person-title{font-size:12px;color:var(--muted);margin-top:2px}
  .contact-list{position:absolute;left:34px;top:72px;list-style:none;color:var(--ink-light);font-size:12.5px;line-height:19px}
  .contact-list li{display:flex;align-items:center;gap:8px}
  .contact-list svg{width:11px;height:11px;fill:var(--ink-light)}
  .address{position:absolute;left:260px;top:92px;color:var(--ink-light);font-size:13px;line-height:18px}
  /* back */
  .card-back{background:radial-gradient(ellipse at 45% 25%,var(--red-light),var(--red) 55%,var(--red-dark))}
  .back-spot{position:absolute;left:50%;top:60px;width:110px;height:110px;margin-left:-55px;border-radius:50%;background:var(--gold);opacity:.9}
  .back-brand{position:absolute;left:0;right:0;bottom:44px;text-align:center;font-family:"Cinzel",serif;font-weight:600;color:var(--red-dark);line-height:1}
  .back-brand .brand-main{display:block;font-size:38px;letter-spacing:1px}
  .back-brand .brand-sub{display:block;font-size:15px;margin-top:6px}
</style>
</head>
<body>
  <section class="card card-front">
    <div class="gold-corner"></div>
    <div class="front-brand">
      <span class="brand-main">HEARTHWALL</span>
      <span class="brand-sub">SECURITY SYSTEMS INC.</span>
    </div>
    <div class="front-band">
      <div class="person">
        <div class="person-name">Daniel Reyes</div>
        <div class="person-title">Founder</div>
      </div>
      <ul class="contact-list">
        <li><svg viewBox="0 0 10 10"><rect x="1" y="1" width="8" height="8" rx="1"/></svg>+698 41 20 20</li>
        <li><svg viewBox="0 0 10 10"><rect x="2.5" y="0.5" width="5" height="9" rx="1"/></svg>+698 63 15 09</li>
        <li><svg viewBox="0 0 10 10"><path d="M0 2h10v6H0z M0 2l5 3.5L10 2" stroke="#9a1f1b" stroke-width=".8"/></svg>info@hearthwall.com</li>
        <li><svg viewBox="0 0 10 10"><circle cx="5" cy="5" r="4.5"/></svg>www.hearthwall.com</li>
      </ul>
      <div class="address">Here your company<br>or home address</div>
    </div>
    <div class="logo-spot"></div>
  </section>

  <section class="card card-back">
    <div class="back-spot"></div>
    <div class="back-brand">
      <span class="brand-main">HEARTHWALL</span>
      <span class="brand-sub">SECURITY SYSTEMS INC.</span>
    </div>
  </section>
</body>
</html>
```